Breezeway Masters Business Card Design

Design new, 2 sides, business cards for a residential and light commercial heating, air conditioning contractor.

Target Market(s)

Homeowners, small businesses

Industry/Entity Type

Business

Contact Information for Business Card

Dominic Halvorsen
Phone - 862-415-2763
Email
Address - PO box 648
Succasunna NJ 07876
Website - www.BreezewayMastersLLC.example

Requirements
Must have
• logo, company colors, standard size with no die cut, so I can use nimbo press

```html
<!DOCTYPE html>
<html lang="en">
<head>
<meta charset="utf-8">
<title>Breezeway Masters Business Card</title>
<link rel="stylesheet" href="https://fonts.googleapis.com/css2?family=Open+Sans:ital,wght@0,400;0,600;1,400&display=swap">
<style>
  :root {
    --brand-red: #9c1f32;
    --brand-orange: #f0921e;
    --ink: #3f3f3f;
    --paper: #ffffff;
    --backdrop: #e9e7e4;
  }
  html, body {
    margin: 0;
    padding: 0;
    width: 1200px;
    height: 987px;
    overflow: hidden;
    background: var(--backdrop);
    font-family: "Open Sans", Arial, sans-serif;
  }
  .canvas {
    position: relative;
    width: 1200px;
    height: 987px;
  }
  .card {
    position: absolute;
    left: 293px;
    width: 615px;
    height: 349px;
    overflow: hidden;
    box-shadow: 0 3px 8px rgba(0,0,0,0.25);
  }
  .card--front { top: 131px; background: var(--paper); }
  .card--back { top: 506px; background: var(--brand-red); }

  .brand-name {
    position: absolute;
    margin: 0;
    font-weight: 600;
    white-space: nowrap;
    display: flex;
    align-items: center;
    gap: 10px;
    line-height: 1.2;
  }
  .brand-name__dot {
    width: 14px;
    height: 14px;
    border-radius: 50%;
    background: var(--brand-orange);
    flex: none;
  }
  .card--front .brand-name {
    right: 31px;
    top: 68px;
    font-size: 28px;
    color: var(--brand-red);
  }
  .card--back .brand-name {
    left: 0;
    right: 0;
    top: 152px;
    justify-content: center;
    font-size: 44px;
    color: var(--paper);
  }

  .person {
    position: absolute;
    left: 35px;
    top: 142px;
  }
  .person__name {
    margin: 0;
    font-size: 21px;
    font-weight: 600;
    color: var(--brand-red);
    line-height: 25px;
  }
  .person__title {
    margin: 0;
    font-size: 16px;
    line-height: 22px;
    color: var(--brand-orange);
  }
  .rule {
    position: absolute;
    left: 35px;
    top: 193px;
    width: 549px;
    height: 1.5px;
    background: var(--brand-orange);
  }
  .contacts {
    position: absolute;
    left: 35px;
    top: 207px;
    margin: 0;
    padding: 0;
    list-style: none;
    font-size: 15px;
    color: var(--ink);
    line-height: 22.5px;
  }
  .contacts li { display: flex; align-items: center; gap: 8px; }
  .contacts svg { width: 15px; height: 15px; fill: var(--brand-red); flex: none; }
  .address {
    position: absolute;
    right: 31px;
    top: 251px;
    margin: 0;
    font-style: normal;
    text-align: right;
    font-size: 15px;
    line-height: 22.5px;
    color: var(--ink);
  }
  .footer-bands {
    position: absolute;
    left: 0;
    bottom: 0;
    width: 615px;
    height: 36px;
  }
  .website {
    position: absolute;
    right: 36px;
    bottom: 6px;
    margin: 0;
    font-size: 16px;
    font-style: italic;
    color: var(--paper);
    letter-spacing: 0.3px;
  }
  .tagline {
    position: absolute;
    left: 0;
    right: 0;
    top: 279px;
    margin: 0;
    text-align: center;
    font-size: 16px;
    font-style: italic;
    color: var(--paper);
    line-height: 21px;
  }
</style>
</head>
<body>
<main class="canvas">

  <section class="card card--front" aria-label="Business card front">
    <p class="brand-name"><span class="brand-name__dot"></span>Breezeway Masters</p>

    <div class="person">
      <h1 class="person__name">DOMINIC HALVORSEN</h1>
      <p class="person__title">CEO/Founder</p>
    </div>
    <div class="rule"></div>

    <ul class="contacts">
      <li>
        <svg viewBox="0 0 16 16" aria-hidden="true"><path d="M3.6 1.2l2.3 2.6-1.3 1.9c.9 2 2.6 3.7 4.6 4.6l1.9-1.3 2.6 2.3-1.3 2.6C7 13.4 2.6 9 1 3.1z"/></svg>
        555 010 0142
      </li>
      <li>
        <svg viewBox="0 0 16 16" aria-hidden="true"><path d="M4.5 0.5h7a1 1 0 0 1 1 1v13a1 1 0 0 1-1 1h-7a1 1 0 0 1-1-1v-13a1 1 0 0 1 1-1zm1 2v9.5h5V2.5z"/></svg>
        555 010 0187
      </li>
      <li>
        <svg viewBox="0 0 16 16" aria-hidden="true"><path d="M4 1h8v4H4zM1 6h14v7h-2v-2H3v2H1zM4 12h8v3H4z"/></svg>
        555 010 0163
      </li>
      <li>
        <svg viewBox="0 0 16 16" aria-hidden="true"><path d="M1 3.5h14v9H1zM1.8 4.2L8 9l6.2-4.8" stroke="#fff" stroke-width="1"/></svg>
        name@breezewaymasters.example
      </li>
    </ul>

    <address class="address">
      PO box 000<br>
      Fairhollow, ST 00000
    </address>

    <svg class="footer-bands" viewBox="0 0 615 36" aria-hidden="true">
      <polygon points="0,18 358,18 350,26 0,26" fill="var(--brand-orange)"/>
      <polygon points="0,28 348,28 346,30 0,30" fill="var(--brand-orange)"/>
      <polygon points="380,0 615,0 615,36 344,36" fill="var(--brand-red)"/>
    </svg>
    <p class="website">breezewaymasters.example</p>
  </section>

  <section class="card card--back" aria-label="Business card back">
    <p class="brand-name"><span class="brand-name__dot"></span>Breezeway Masters</p>
    <p class="tagline">Residential &amp; light commercial heating<br>Air conditioning contractor</p>
  </section>

</main>
</body>
</html>
```